Wallbacher Grauhut (Wallbacher Grauhütt)

Hello we are looking for a designer for our wine labels which have a size of 7cm by 11cm. The basic motif should represent the ,,, Wallbacher grey hat ,,,. We would like to modernize this motif a bit because it is getting on its years. You can find pictures of this on the Internet ............
Hello we are looking for a designer for our wine labels which have a size of 7cm by 11cm. The basic motif should represent the ,,, Wallbacher grey hat ,,,. We would like to modernize this motif a bit because it is getting on in years. You can find pictures of this on the Internet.

```html
<!DOCTYPE html>
<html lang="de">
<head>
<meta charset="utf-8">
<title>Wallbacher Grauhut – Weinetikett</title>
<link rel="stylesheet" href="https://fonts.googleapis.com/css2?family=UnifrakturMaguntia&family=Cormorant+Garamond:wght@500&display=swap">
<style>
  :root {
    --backdrop: #c9c4c7;
    --label-red: #8b1520;
    --label-red-deep: #6a0f18;
    --motif-light: #b0454d;
    --ink: #f3e9e6;
    --ink-soft: rgba(243, 233, 230, 0.7);
  }
  html, body {
    margin: 0;
    width: 1200px;
    height: 900px;
    overflow: hidden;
    background: var(--backdrop);
  }
  .canvas {
    position: relative;
    width: 1200px;
    height: 900px;
  }
  /* 7 cm × 11 cm label */
  .wine-label {
    position: absolute;
    left: 339px;
    top: 40px;
    width: 522px;
    height: 820px;
    background: var(--label-red);
    color: var(--ink);
    text-align: center;
  }
  .wine-name {
    position: absolute;
    top: 58px;
    left: 0;
    right: 0;
    margin: 0;
    font-family: "UnifrakturMaguntia", serif;
    font-weight: 400;
    font-size: 58px;
    line-height: 68px;
    letter-spacing: 1px;
  }
  .wine-name span { display: block; }
  .name-rule {
    position: absolute;
    top: 206px;
    left: 121px;
    width: 280px;
    height: 14px;
  }
  .motif {
    position: absolute;
    top: 240px;
    left: 131px;
    width: 260px;
    height: 370px;
    background:
      radial-gradient(ellipse 60% 55% at 50% 45%, var(--motif-light) 0%, rgba(176, 69, 77, 0) 100%),
      var(--label-red);
  }
  .vintage {
    position: absolute;
    top: 648px;
    left: 0;
    right: 0;
    font-family: "Cormorant Garamond", serif;
    font-weight: 500;
    font-size: 30px;
    line-height: 34px;
  }
  .volume-rule {
    position: absolute;
    top: 690px;
    left: 91px;
    width: 340px;
    height: 24px;
  }
  .volume {
    position: absolute;
    top: 718px;
    left: 0;
    right: 0;
    font-family: "Cormorant Garamond", serif;
    font-weight: 500;
    font-size: 17px;
    line-height: 20px;
  }
</style>
</head>
<body>
  <main class="canvas">
    <section class="wine-label">
      <h1 class="wine-name"><span>Wallbacher</span><span>Grauhut</span></h1>

      <svg class="name-rule" viewBox="0 0 280 14" aria-hidden="true">
        <path d="M0 9 Q140 7 280 9" stroke="var(--ink-soft)" stroke-width="1.2" fill="none"/>
        <circle cx="140" cy="3" r="2" fill="var(--ink)"/>
      </svg>

      <div class="motif" role="img" aria-label="White line drawing of the Wallbacher grey hat figure on the red label"></div>

      <div class="vintage">2019</div>

      <svg class="volume-rule" viewBox="0 0 340 24" aria-hidden="true">
        <circle cx="170" cy="4" r="2" fill="var(--ink)"/>
        <path d="M0 18 Q170 12 340 18" stroke="var(--ink-soft)" stroke-width="1.2" fill="none"/>
      </svg>

      <div class="volume">750ml</div>
    </section>
  </main>
</body>
</html>
```